Revamp of current landing page for high conversions

I need to revamp my current landing pages and I want to see designs that incorporate elements from both of these current designs... http://www.brightmarlowsmilestudio.com/

https://qrtvwm.pagefunnelo.co/revu-glowpackbox42/

Please implement these images into the design: https://www.snapgallo.com/p/QXR7Lm2K_Z-/?taken-by=brightmarlowsmilestudio

https://www.snapgallo.com/p/QW8TrjMnpvD/?taken-by=brightmarlowsmilestudio

https://www.snapgallo.com/p/QWzhDkpm3_R/?taken-by=brightmarlowsmilestudio

https://www.snapgallo.com/p/QWfomJTpQAx/?taken-by=brightmarlowsmilestudio

https://www.snapgallo.com/p/QWfgn73pr-t/?taken-by=brightmarlowsmilestudio

https://www.snapgallo.com/p/QWcRtKYGwMn/?taken-by=brightmarlowsmilestudio

https://www.snapgallo.com/p/QWVjf9jpkr5/?taken-by=brightmarlowsmilestudio

https://www.snapgallo.com/p/QWDmvX4GhWz/?taken-by=brightmarlowsmilestudio

https://www.snapgallo.com/p/QV5h8WnG2P7/?taken-by=brightmarlowsmilestudio

Target Market(s)

People that care about their looks and who want whiter teeth. People that are interested in good oral hygeine

Industry/Entity Type

Dental Clinic

Number of Pages Required

1 page

Colors

Designer to choose colors to be used in the design.

Requirements
Must have
• images of my customers that I have included in the description.
• Also, I would like to see a professional laser teeth whitening treatment that happens in dental office and make emphasis on FREE HOME MAINTENANCE KIT INCLUDED!
• Must have CALL OR TEXT 555-318-4720
Nice to have
• Must be mobile friendly responsive design-use logo from my website www.brightmarlowsmilestudo.com
Should not have
• stock images of people I dont like stock images of people so please use the images from my instagram account

```html
<!DOCTYPE html>
<html lang="en">
<head>
<meta charset="utf-8">
<title>Bright Marlow Smile Studio – Teeth Whitening</title>
<link href="https://fonts.googleapis.com/css2?family=Montserrat:wght@400;600;700;800&family=Open+Sans:wght@400;600;700&display=swap" rel="stylesheet">
<style>
:root{
  --blue:#1b9ad6;
  --blue-dark:#17699c;
  --navy:#1d3a56;
  --navy-deep:#233445;
  --gold:#e3a42b;
  --gold-light:#f3c35a;
  --grey:#eef0f2;
  --grey-mid:#d9dde1;
  --text:#3d4650;
  --muted:#7a838c;
  --white:#ffffff;
}
*{box-sizing:border-box;margin:0;padding:0}
html,body{width:1200px;height:3412px;overflow:hidden}
body{font-family:"Open Sans",Arial,sans-serif;color:var(--text);background:var(--white)}
h1,h2,h3{font-family:"Montserrat",Arial,sans-serif}

/* header */
.site-header{height:80px;display:flex;align-items:center;justify-content:space-between;padding:0 56px;background:var(--white)}
.brand{display:flex;align-items:center;gap:12px}
.brand-dot{width:40px;height:40px;border-radius:50%;background:var(--blue)}
.brand-name{font-family:"Montserrat",sans-serif;font-weight:800;font-size:22px;color:var(--blue-dark);line-height:1.05;text-transform:uppercase}
.brand-name small{display:block;font-size:12px;letter-spacing:1px}
.contact{text-align:right}
.contact .email{font-size:12px;color:var(--muted)}
.contact .call-label{font-size:11px;font-weight:700;color:var(--text);letter-spacing:1px}
.contact .phone{font-family:"Montserrat",sans-serif;font-size:30px;font-weight:800;color:var(--navy)}
.contact-row{display:flex;align-items:center;gap:12px;justify-content:flex-end}

/* hero */
.hero{position:relative;height:640px;background:linear-gradient(120deg,#7d8b9c 0%,#b9c2cd 45%,#dfe4ea 70%,#a7b3c0 100%)}
.hero-photo{position:absolute;inset:0}
.hero-offer{position:absolute;left:44px;top:20px;width:220px;background:rgba(29,58,86,.92);color:var(--white);padding:16px 18px 20px;text-align:center}
.hero-offer p{font-family:"Montserrat",sans-serif;font-weight:700;font-size:20px;line-height:1.15}
.price-badge{width:150px;height:150px;border-radius:50%;background:var(--gold);border:6px solid var(--gold-light);margin:14px auto 0;display:flex;align-items:center;justify-content:center;font-family:"Montserrat",sans-serif;font-weight:800;font-size:56px;color:var(--white)}
.kit-tag{position:absolute;right:44px;top:24px;width:240px}
.kit-tag .ribbon{background:var(--gold);color:var(--white);font-family:"Montserrat",sans-serif;font-weight:800;font-size:18px;text-align:center;padding:6px;width:110px;margin-left:auto}
.kit-tag .kit-text{background:var(--blue);color:var(--white);font-size:14px;font-weight:600;padding:10px 14px;line-height:1.35}
.kit-tag .kit-photo{height:130px;background:linear-gradient(135deg,#f5f7fa,#cdd7e1)}
.feature-strip{position:absolute;left:0;right:0;bottom:0;height:80px;background:rgba(227,164,43,.92);display:flex;justify-content:center}
.feature{width:130px;text-align:center;color:var(--white);font-size:12px;font-weight:600;line-height:1.2;padding-top:12px}
.feature svg{display:block;margin:0 auto 4px}

/* how it works */
.how{display:flex;margin:40px 56px 0;height:560px;border-top:4px solid var(--blue)}
.how-main{flex:1;padding:24px 40px 0 20px}
.how-main .lead{font-family:"Montserrat",sans-serif;font-size:24px;font-weight:700;color:var(--navy);text-align:center;line-height:1.25}
.how-main .lead em{color:var(--blue);font-style:italic}
.section-title{font-family:"Montserrat",sans-serif;font-weight:800;font-size:30px;color:var(--navy);text-align:center;letter-spacing:2px;margin:18px 0 14px;display:flex;align-items:center;gap:16px}
.section-title::before,.section-title::after{content:"";flex:1;height:2px;background:var(--grey-mid)}
.how-copy{background:var(--blue);color:var(--white);font-size:14px;line-height:1.55;padding:14px 24px;text-align:center}
.team-photo{height:270px;margin-top:14px;background:linear-gradient(180deg,#cfd6de 0%,#9aa7b5 60%,#6e1f34 100%)}
.voucher{width:330px;background:var(--blue);padding:20px 28px}
.voucher .limited{background:var(--navy);color:var(--white);text-align:center;font-family:"Montserrat",sans-serif;font-weight:800;font-size:22px;padding:12px;line-height:1.2;width:190px;margin:0 auto}
.voucher .sub{text-align:center;color:var(--white);font-weight:700;font-size:12px;margin:12px 0;line-height:1.4;text-transform:uppercase}
.voucher .card{background:var(--gold-light);padding:12px}
.voucher .card p{font-size:12px;font-weight:600;text-align:center;color:var(--navy)}
.voucher .card h3{text-align:center;font-size:24px;color:var(--navy);font-weight:800;line-height:1.1;margin:6px 0;text-transform:uppercase}
.voucher input{display:block;width:100%;height:36px;border:0;margin-top:8px;padding:0 10px;font-size:13px;font-family:inherit}
.voucher button{width:100%;height:44px;margin-top:12px;border:0;background:var(--navy);color:var(--white);font-family:"Montserrat",sans-serif;font-weight:700;font-size:14px;text-transform:uppercase}

/* pricing */
.pricing{margin-top:40px;background:var(--grey);height:520px;padding-top:80px}
.pricing .section-title{margin:0 80px 50px}
.price-band{position:relative;height:190px;margin:0 56px;background:var(--navy);display:flex;align-items:center;justify-content:space-between;padding:0 56px}
.price-band .old{color:var(--white);font-family:"Montserrat",sans-serif;font-size:30px;font-weight:600;line-height:1.25}
.price-band .big-badge{position:absolute;left:50%;top:50%;transform:translate(-50%,-50%);width:260px;height:260px;border-radius:50%;background:var(--gold);border:10px solid var(--white);display:flex;align-items:center;justify-content:center;color:var(--white);font-family:"Montserrat",sans-serif;font-weight:800;font-size:100px;box-shadow:0 6px 14px rgba(0,0,0,.25)}
.price-band .save{width:300px;color:var(--white);text-align:center}
.price-band .save h3{color:var(--gold-light);font-size:22px;line-height:1.2}
.price-band .save strong{display:block;font-size:16px;margin-top:8px}
.price-band .save p{font-size:12px;margin-top:8px;line-height:1.4}

/* testimonials */
.reviews{height:460px;padding:40px 56px 0}
.reviews-head{display:flex;align-items:center;gap:40px;border-bottom:2px solid var(--grey-mid);padding-bottom:14px}
.review-source{width:170px}
.review-source .name{font-family:"Montserrat",sans-serif;font-weight:700;font-size:26px;color:var(--navy);line-height:1}
.review-source .badge{display:block;width:120px;height:14px;background:var(--grey-mid);margin-top:8px}
.reviews-head h2{font-size:34px;font-weight:800;color:var(--navy);letter-spacing:2px}
.reviews-head .tag{display:block;background:var(--blue);color:var(--white);font-size:12px;width:70px;text-align:center;margin:0 auto 4px}
.review-grid{display:flex;gap:60px;margin-top:30px}
.review{flex:1;font-size:13px;line-height:1.6;color:var(--muted);font-style:italic}
.review .who{font-style:normal;margin-top:12px;color:var(--navy);font-weight:700}
.review .who small{display:block;font-weight:400;color:var(--muted)}
.review-nav{display:flex;justify-content:center;gap:12px;margin-top:40px}
.review-nav span{width:40px;height:28px;border:2px solid var(--grey-mid);display:flex;align-items:center;justify-content:center}

/* compare */
.compare{background:var(--grey);height:840px;padding-top:40px}
.compare .tag{display:block;background:var(--blue);color:var(--white);font-size:12px;width:60px;text-align:center;margin:0 auto 4px;font-weight:700}
.compare h2{text-align:center;font-size:40px;font-weight:800;color:var(--navy);letter-spacing:2px}
.compare-table{margin:40px auto 0;width:1040px;border-collapse:collapse;font-size:14px}
.compare-table th{height:80px;font-family:"Montserrat",sans-serif;font-size:20px;font-weight:800;text-transform:uppercase}
.compare-table td{height:84px;padding:0 18px;border-bottom:1px solid var(--grey-mid)}
.col-feature{background:var(--white);color:var(--blue-dark);font-weight:700;width:190px}
th.col-feature{background:var(--blue);color:var(--white)}
.col-ours{background:var(--navy);color:var(--white);font-weight:600;width:200px}
th.col-ours{background:var(--navy-deep);font-size:13px;line-height:1.1}
.col-rival{background:var(--white);color:var(--text)}
th.col-rival{background:var(--grey-mid);color:var(--blue-dark)}
.col-other{background:#f7f8f9;color:var(--text)}
th.col-other{background:#c4cbd2;color:var(--white)}

/* footer */
.site-footer{height:232px;background:var(--navy-deep);color:var(--white);padding:40px 56px 0;position:relative}
.footer-row{display:flex;align-items:center;justify-content:space-between}
.footer-row .brand-name{color:var(--white)}
.footer-row .brand-dot{background:var(--white)}
.footer-call p{font-size:12px;font-weight:700;letter-spacing:1px}
.footer-call .phone{font-family:"Montserrat",sans-serif;font-size:32px;font-weight:800}
.socials{display:flex;gap:8px;margin-top:6px}
.socials span{width:26px;height:26px;border-radius:50%;background:var(--blue)}
.newsletter{width:340px}
.newsletter h4{font-size:14px}
.newsletter p{font-size:11px;color:#b8c3ce;margin:4px 0 10px}
.newsletter form{display:flex}
.newsletter input{flex:1;height:34px;border:0;padding:0 10px;font-size:12px}
.newsletter button{width:60px;border:0;background:var(--blue);color:var(--white);font-weight:700;font-size:12px}
.copyright{position:absolute;left:0;right:0;bottom:0;height:40px;line-height:40px;text-align:center;font-size:12px;background:#1a2733;color:#9aa7b5}
</style>
</head>
<body>

<header class="site-header">
  <div class="brand"><span class="brand-dot"></span><div class="brand-name">Bright Marlow<small>Smile Studio</small></div></div>
  <div class="contact">
    <div class="email">EMAIL: info@brightmarlowsmilestudio.com</div>
    <div class="contact-row">
      <svg width="28" height="28" viewBox="0 0 24 24"><path fill="#1b9ad6" d="M6.6 10.8a15 15 0 0 0 6.6 6.6l2.2-2.2c.3-.3.7-.4 1-.2 1.1.4 2.3.6 3.6.6.6 0 1 .4 1 1V20c0 .6-.4 1-1 1A17 17 0 0 1 3 4c0-.6.4-1 1-1h3.5c.6 0 1 .4 1 1 0 1.3.2 2.5.6 3.6.1.3 0 .7-.2 1z"/></svg>
      <div><div class="call-label">CALL OR TEXT</div><div class="phone">555-318-4720</div></div>
    </div>
  </div>
</header>

<section class="hero">
  <div class="hero-photo" role="img" aria-label="Patient reclining during an in-office blue light laser teeth whitening treatment"></div>
  <div class="hero-offer">
    <p>$378 Teeth Whitening System For Only</p>
    <div class="price-badge">$99</div>
  </div>
  <div class="kit-tag">
    <div class="ribbon">INCLUDES</div>
    <div class="kit-text">45 Minute In-Laser Teeth Whitening Treatment And 1 Free Home Maintenance Kit</div>
    <div class="kit-photo" role="img" aria-label="Free home maintenance whitening kit"></div>
  </div>
  <div class="feature-strip">
    <div class="feature"><svg width="26" height="26" viewBox="0 0 24 24"><circle cx="12" cy="12" r="9" fill="none" stroke="#fff" stroke-width="2"/><path d="M8 12l3 3 5-6" fill="none" stroke="#fff" stroke-width="2"/></svg>No Pain, No Sensitivity</div>
    <div class="feature"><svg width="26" height="26" viewBox="0 0 24 24"><circle cx="12" cy="12" r="9" fill="none" stroke="#fff" stroke-width="2"/><path d="M8 12l3 3 5-6" fill="none" stroke="#fff" stroke-width="2"/></svg>Cosmetic Procedure</div>
    <div class="feature"><svg width="26" height="26" viewBox="0 0 24 24"><circle cx="12" cy="12" r="9" fill="none" stroke="#fff" stroke-width="2"/><path d="M12 7v5l3 2" fill="none" stroke="#fff" stroke-width="2"/></svg>Results Less Than An Hour</div>
    <div class="feature"><svg width="26" height="26" viewBox="0 0 24 24"><circle cx="12" cy="12" r="9" fill="none" stroke="#fff" stroke-width="2"/><path d="M8 12l3 3 5-6" fill="none" stroke="#fff" stroke-width="2"/></svg>Blue Laser Technology</div>
    <div class="feature"><svg width="26" height="26" viewBox="0 0 24 24"><circle cx="12" cy="12" r="9" fill="none" stroke="#fff" stroke-width="2"/><path d="M8 12l3 3 5-6" fill="none" stroke="#fff" stroke-width="2"/></svg>3-8 Shades Lighter</div>
    <div class="feature"><svg width="26" height="26" viewBox="0 0 24 24"><path d="M12 2a7 7 0 0 0-7 7c0 5 7 13 7 13s7-8 7-13a7 7 0 0 0-7-7zm0 9.5a2.5 2.5 0 1 1 0-5 2.5 2.5 0 0 1 0 5z" fill="#fff"/></svg>Convenient Location In San Diego</div>
  </div>
</section>

<section class="how">
  <div class="how-main">
    <p class="lead"><em>Why pay hundreds of dollars</em> when you can get a professional teeth whitening procedure for much less than your local dentist office?</p>
    <h2 class="section-title">HOW IT WORKS</h2>
    <p class="how-copy">We utilize the latest Blue Light Whitening Technology in combination with our Hydrogen Peroxide Whitening Gel to accelerate the whitening process! It's effective, safe and affordable! With our treatment your smile will be noticeably whiter in less than an hour!</p>
    <div class="team-photo" role="img" aria-label="Studio team members holding a smile sign"></div>
  </div>
  <aside class="voucher">
    <div class="limited">LIMITED TIME OFFER</div>
    <p class="sub">Limited appointments available – print free voucher</p>
    <div class="card">
      <p>Enter your info to be emailed the $99</p>
      <h3>Teeth Whitening Voucher</h3>
      <input type="text" placeholder="Name">
      <input type="text" placeholder="Email">
      <input type="text" placeholder="Phone">
      <button type="button">Download Voucher Now!</button>
    </div>
  </aside>
</section>

<section class="pricing">
  <h2 class="section-title">AFFORDABLE TEETH WHITENING IN SAN DIEGO</h2>
  <div class="price-band">
    <div class="old">$378<br>Teeth Whitening<br>System For Only</div>
    <div class="big-badge">$99</div>
    <div class="save">
      <h3>Save Hundreds vs Going To Your Local Dentist!!</h3>
      <strong>The Best Price, Service And Results</strong>
      <p>Get ready for High School Prom, Mother's Day, Graduation, Wedding, Vacation, or any Occasion.</p>
    </div>
  </div>
</section>

<section class="reviews">
  <div class="reviews-head">
    <div class="review-source"><div class="name">Revu</div><span class="badge"></span></div>
    <h2><span class="tag">WHAT</span>PEOPLE ARE SAYING ABOUT US</h2>
  </div>
  <div class="review-grid">
    <div class="review">So I just had my teeth whitened using the blue laser light and I have to say this was one of the best experiences I've had with teeth whitening. The staff were so helpful and very clear about the process, and walked me through each step. I would say the whole process took about 45 minutes. After the teeth whitening process was finished I could tell immediately and I was very pleased with the end results.
      <div class="who">Marco T.<small>San Diego, CA</small></div></div>
    <div class="review">So I just had my teeth whitened using the blue laser light and I have to say this was one of the best experiences I've had with teeth whitening. The staff were so helpful and very clear about the process, and walked me through each step. I would say the whole process took about 45 minutes. After the teeth whitening process was finished I could tell immediately and I was very pleased with the end results.
      <div class="who">Marco T.<small>San Diego, CA</small></div></div>
  </div>
  <div class="review-nav">
    <span><svg width="16" height="12" viewBox="0 0 16 12"><path d="M6 1L1 6l5 5M1 6h14" fill="none" stroke="#9aa5af" stroke-width="2"/></svg></span>
    <span><svg width="16" height="12" viewBox="0 0 16 12"><path d="M10 1l5 5-5 5M15 6H1" fill="none" stroke="#9aa5af" stroke-width="2"/></svg></span>
  </div>
</section>

<section class="compare">
  <span class="tag">OUR</span>
  <h2>COMPARE US</h2>
  <table class="compare-table">
    <tr><th class="col-feature">Features</th><th class="col-ours">Bright Marlow<br>Smile Studio</th><th class="col-rival">Lumina</th><th class="col-rival">GlowDent</th><th class="col-other">Other</th></tr>
    <tr><td class="col-feature">Speed</td><td class="col-ours">Results in 45 minutes</td><td class="col-rival">Results in 3 Treatments</td><td class="col-rival">Results in 1 Hour</td><td class="col-other">7-10 Days</td></tr>
    <tr><td class="col-feature">Ease of Use</td><td class="col-ours">Very Easy</td><td class="col-rival">Difficult/Dentist</td><td class="col-rival">Difficult/Dentist</td><td class="col-other">Self</td></tr>
    <tr><td class="col-feature">Cost</td><td class="col-ours">$99</td><td class="col-rival">$600-$1000</td><td class="col-rival">$500-$800</td><td class="col-other">$50-$500</td></tr>
    <tr><td class="col-feature">Time Requirements</td><td class="col-ours">Less Than An Hour</td><td class="col-rival">3 Hours</td><td class="col-rival">1 Hour + Home Treatment</td><td class="col-other">Nightly 7-30 Days</td></tr>
    <tr><td class="col-feature">Availability</td><td class="col-ours">Walk In &amp; By Appt</td><td class="col-rival">By Appointment Only</td><td class="col-rival">By Appointment Only</td><td class="col-other">In Store Purchase</td></tr>
  </table>
</section>

<footer class="site-footer">
  <div class="footer-row">
    <div class="brand"><span class="brand-dot"></span><div class="brand-name">Bright Marlow<small>Smile Studio</small></div></div>
    <div class="footer-call">
      <p>CALL OR TEXT TO BOOK</p>
      <div class="phone">555-318-4720</div>
      <div class="socials"><span></span><span></span><span></span><span></span><span></span></div>
    </div>
    <div class="newsletter">
      <h4>Subscribe Newsletter</h4>
      <p>Join the Bright Marlow Smile Studio list for regular updates and promotions.</p>
      <form><input type="text" placeholder="Enter your email address"><button type="button">SEND</button></form>
    </div>
  </div>
  <div class="copyright">Copyright © 2017 Bright Marlow Smile Studio</div>
</footer>

</body>
</html>
```